Letterhead for Conveyancing Company

Use existing logo to create a letterhead for a conveyancing company. Must be able to be used in Microsoft Word. Easy to read and professional.
Contact information to be at the bottom.
Brightwater Conveyancing Pty Ltd
ACN 621 984 736PO Box 535 Campbelltown SA 5074
Mobile - 0461 739 285
Web address - www.brightwaterconveyancing.com.au

Requirements
Must have
• Logo and contact details.
• Simple and professional.

```html
<!DOCTYPE html>
<html lang="en">
<head>
<meta charset="utf-8">
<title>Brightwater Conveyancing – Letterhead</title>
<link rel="stylesheet" href="https://fonts.googleapis.com/css2?family=Lato:wght@400;700&family=Open+Sans:wght@400;600&display=swap">
<style>
  :root {
    --brand-pink: #e0409a;
    --brand-grey: #7d7d7d;
    --ink: #3a3a3a;
    --ink-soft: #505050;
    --paper: #ffffff;
  }
  html, body {
    margin: 0;
    padding: 0;
    width: 1040px;
    height: 1200px;
    overflow: hidden;
    background: var(--paper);
  }
  .letterhead {
    position: relative;
    width: 1040px;
    height: 1200px;
    background: var(--paper);
    font-family: "Open Sans", sans-serif;
    color: var(--ink-soft);
  }
  .brand-name {
    position: absolute;
    left: 99px;
    top: 58px;
    display: flex;
    align-items: center;
    gap: 12px;
    font-family: "Lato", sans-serif;
    font-weight: 700;
    font-size: 38px;
    color: var(--brand-pink);
    letter-spacing: -0.5px;
  }
  .brand-mark {
    width: 22px;
    height: 22px;
    background: var(--brand-grey);
  }
  .company-details {
    position: absolute;
    left: 608px;
    top: 38px;
    padding-left: 18px;
    border-left: 2px solid var(--brand-pink);
    font-family: "Lato", sans-serif;
    font-size: 18px;
    line-height: 22px;
    color: #111;
  }
  .company-details .company-title { color: var(--brand-pink); }
  .letter-meta {
    position: absolute;
    left: 99px;
    font-size: 15px;
    line-height: 18px;
  }
  .issue-date { top: 222px; }
  .recipient { top: 258px; }
  .salutation { top: 362px; }
  .letter-body {
    position: absolute;
    left: 99px;
    top: 412px;
    width: 838px;
    font-size: 15px;
    line-height: 27px;
    text-align: justify;
    hyphens: auto;
  }
  .letter-body p { margin: 0 0 27px; }
  .sign-off { position: absolute; left: 99px; top: 820px; font-size: 15px; }
  .signatory-name {
    position: absolute; left: 99px; top: 893px;
    font-size: 19px; font-weight: 600; color: var(--ink);
  }
  .signatory-role { position: absolute; left: 99px; top: 925px; font-size: 15px; }
  .footer-band {
    position: absolute;
    left: 0;
    top: 1146px;
    width: 1040px;
    height: 54px;
  }
  .footer-phone, .footer-web {
    position: absolute;
    font-family: "Lato", sans-serif;
    color: #fff;
    font-size: 18px;
  }
  .footer-phone { left: 100px; top: 1168px; }
  .footer-phone b { font-weight: 700; }
  .footer-web { right: 104px; top: 1158px; font-weight: 700; }
</style>
</head>
<body>
<div class="letterhead">
  <div class="brand-name"><span class="brand-mark"></span>Brightwater</div>

  <div class="company-details">
    <div class="company-title">Brightwater Conveyancing Pty Ltd</div>
    <div>ACN 738 215 409</div>
    <div>PO Box 812 Glenhaven SA 5091</div>
  </div>

  <div class="letter-meta issue-date">Issuing Date: May 5, 2018</div>
  <div class="letter-meta recipient">Name Of Employee Mr. XYZABC<br>Address of Employee<br>Address Line 2 etc..</div>
  <div class="letter-meta salutation">Dear Mr.XYZABC</div>

  <div class="letter-body">
    <p>Lorem Ipsum has been the industry's standard dummy text ever since the 1500s, when an unknown printer took a galley of type and scrambled it to make a type specimen book. It has survived not only five centuries, but also the leap into electronic typesetting, remaining essentially unchanged. It was popularised in the 1960s with the release of Lettrex sheets containing Lorem Ipsum passages, and more recently with desktop publishing software like Pageline Studio including versions of Lorem Ipsum.</p>
    <p>Lorem Ipsum is simply dummy text of the printing and typesetting industry. Lorem Ipsum has been the industry's standard dummy text ever since the 1500s, when an unknown printer took a galley of type and scrambled it to make a type specimen book.</p>
    <p>It has survived not only five centuries, but also the leap into electronic typesetting, remaining essentially unchanged. It was popularised in the 1960s with the release of Lettrex sheets containing Lorem IpsumIpsum passages.</p>
  </div>

  <div class="sign-off">Yours Sincerely</div>
  <div class="signatory-name">Daniel Hartley</div>
  <div class="signatory-role">Managing Director</div>

  <svg class="footer-band" viewBox="0 0 1040 54" aria-hidden="true">
    <polygon points="509,0 1040,0 1040,46 484,46" fill="var(--brand-grey)"/>
    <polygon points="0,12 497,12 473,54 0,54" fill="var(--brand-pink)"/>
  </svg>
  <div class="footer-phone"><b>P:</b> 0461 739 285</div>
  <div class="footer-web">www.brightwaterconveyancing.com.au</div>
</div>
</body>
</html>
```